Young, funky marketing collateral and other stuff
Exciting and innovative ideas welcomed
We are thrilled with the designs that have come in and are now spoilt for choice as they are all individually very good. We appreciate the trouble you have gone to in response to our direct feedback as we 'fine tune' our ideas. Thanks designers, you are all great.
A big thank you also to Owen in Support who has helped to smooth the way between us and the designers when we have run into difficulty conveying some of our ideas.
Have already recommended Tallowspan to others
Regards
RTolley
Fernwick logo
#14: the way that the fernwick logo colours have been made neutral is very good and perfectly acceptable to us.
A general reminder; fernwick logo only on biz card, folder, letterhead and signature. Not on other things.
Address Label:
#13 has the right idea for the address label, however we would like it to be landscape design rather than portrait
Yard signs: it would be good to have the branding colours 'frame' the signs in some way too thanks. Thanks for your great efforts.
Hi Designers
On the yard signs, please include as part of the branding template:
www.kvtp.co.nz
Thanks
Clarification on Registry. Please use the following 'Open for Inspection Registry' not 'Open House Registry'. Thanks.
Also, the Registry does not require fernwick logo.
Brightnook, thanks for your ideas. #4 is attractive, we prefer the way you have presented the company address in the letterhead, by contrast in #3 the company address in footer looks a bit staggered and not so smart. The logo reflection on the #4 folder is also very appealing.
#5 Thank you for your new design.
The address label; please make the dot dot lines in the receiver's address longer and more central. We will be handwriting the receiver's address on the dot dot line and it needs to have enough space to do this and so that a courier or post office can read the address and deliver the package easily.
Thanks for the new designs. I can see that trying to incorporate the 2nd logo (fernwick property) is simply going to cause confusion however we do need somehow to represent the second company. Instead of using logo, please just use company name and designation which is 'Fernwick Property Ltd, Licensed Agent (PLNB) 2008. Please include this on the business card, folder, letterhead, and signature. It would be suitable to have it, for instance, in the bottom line of the footer, the two company names as bullet points.
@DW - please check your private message on top right corner after clicking messages once you log in. Thanks
A big thanks to pixvellor for starting of the process with neat designs #1 and #2.
My brief may not have been totally clear so here are a couple more thoughts:
The mailing label: There needs to be a space (........... line) after 'company/name etc so that the sender can hand write the details in. For example:
Company/Name ...........................................
Address .................................................
.........................................................City ....................................................
Phone ...................................................
Attention ...............................................
Please also note my comment at start of brief about also including Fernwick property details on some of the collateral. If it's going to look too crowded, just use the fernwick logo.
On the 'inspect today' sign, the 'inspect today' plus arrow are major components, the branding is minor. This sign will be placed at intersections directing buyers to a home, so the size of the arrow is important.
Thanks everyone and we look forward to seeing your ideas.

```html
<!DOCTYPE html>
<html lang="en">
<head>
<meta charset="utf-8">
<title>Kestrel Vale Realty – Stationery</title>
<link href="https://fonts.googleapis.com/css2?family=Open+Sans:ital,wght@0,400;0,600;0,700;1,600&display=swap" rel="stylesheet">
<style>
:root{
  --bg:#eceef0;
  --paper:#ffffff;
  --blue:#2a9fd8;
  --blue-light:#62c4ef;
  --blue-deep:#1b7fb8;
  --charcoal:#3b4045;
  --ink:#2b2f33;
  --muted:#7b8288;
}
*{box-sizing:border-box;margin:0;padding:0}
html,body{width:1200px;height:961px;overflow:hidden}
body{background:var(--bg);font-family:"Open Sans",Arial,sans-serif;color:var(--ink);position:relative}
.sheet{position:absolute;box-shadow:0 4px 14px rgba(0,0,0,.18);overflow:hidden;background:var(--paper)}
.wave{position:absolute;left:0;width:100%;display:block}
.brand{display:flex;align-items:center;gap:8px;font-weight:700;color:var(--blue-deep);letter-spacing:.02em}
.brand-mark{background:currentColor;flex:none}
.brand.on-blue{color:#fff}

/* folder */
.folder{position:absolute;left:104px;top:117px;width:586px;height:715px}
.folder-panel{position:absolute;top:0;width:293px;height:490px;overflow:hidden;box-shadow:0 4px 14px rgba(0,0,0,.18)}
.folder-back{left:0;background:linear-gradient(180deg,var(--blue-light),var(--blue) 60%,var(--blue-deep))}
.folder-front{left:293px;background:var(--paper)}
.folder-back .brand{position:absolute;left:26px;top:318px;font-size:15px}
.folder-back .brand-mark{width:22px;height:22px}
.folder-address{position:absolute;left:26px;top:352px;color:#fff;font-size:8.5px;line-height:1.55}
.folder-address strong{font-weight:700}
.folder-front .brand{position:absolute;left:0;right:0;top:118px;justify-content:center;font-size:22px}
.folder-front .brand-mark{width:34px;height:34px}
.tagline{position:absolute;left:0;right:0;top:362px;text-align:center;font-style:italic;font-weight:600;font-size:15px;color:var(--ink)}
.folder-url{position:absolute;right:22px;bottom:16px;font-size:9px;color:#fff}
.pocket{position:absolute;top:490px;width:293px;height:225px;background:linear-gradient(180deg,var(--blue),var(--blue-deep));box-shadow:0 4px 14px rgba(0,0,0,.18)}
.pocket-left{left:0;clip-path:polygon(0 0,100% 0,100% 55%,88% 100%,0 100%)}
.pocket-right{left:293px;clip-path:polygon(0 0,100% 0,100% 100%,12% 100%,0 55%)}
.pocket-mark{position:absolute;top:82px;width:30px;height:30px;background:#fff}
.pocket-left .pocket-mark{left:131px}
.pocket-right .pocket-mark{left:131px}

/* letterhead */
.letterhead{left:754px;top:117px;width:312px;height:481px}
.letterhead .brand{position:absolute;left:22px;top:26px;font-size:13px}
.letterhead .brand-mark{width:18px;height:18px}
.letter-tag{position:absolute;right:18px;top:22px;font-size:6px;font-style:italic;font-weight:600;color:var(--muted)}
.letter-body{position:absolute;left:22px;right:22px;top:86px;font-size:5.6px;line-height:1.7;color:#555}
.letter-body p{margin-bottom:8px}
.signature-line{width:60px;height:12px;border-bottom:1px solid #666;margin:6px 0 3px}
.letter-footer{position:absolute;left:22px;bottom:8px;font-size:5.6px;color:#fff}

/* cards */
.card{width:130px;height:68px}
.card-front{left:767px;top:767px}
.card-back{left:910px;top:767px}
.card .brand{position:absolute;left:10px;top:18px;font-size:9px}
.card .brand-mark{width:12px;height:12px}
.card-back .brand{left:auto;right:10px;top:8px;font-size:7px}
.card-back .brand-mark{width:9px;height:9px}
.card-details{position:absolute;left:10px;top:26px;font-size:5.2px;line-height:1.5;color:var(--ink)}
.card-details strong{font-size:6px}

/* compliments slip */
.slip{left:767px;top:871px;width:299px;height:65px}
.slip .brand{position:absolute;left:14px;top:14px;font-size:12px}
.slip .brand-mark{width:16px;height:16px}
.slip-details{position:absolute;left:160px;top:14px;font-size:6px;line-height:1.5}

/* registry */
.registry{left:234px;top:845px;width:377px;height:91px}
.registry h1{position:absolute;left:20px;top:10px;font-size:19px;font-weight:700;color:var(--ink)}
.registry h2{position:absolute;left:150px;top:38px;font-size:11px;font-weight:600;color:var(--ink)}
</style>
</head>
<body>

<section class="folder" aria-label="Presentation folder">
  <div class="folder-panel folder-back">
    <svg class="wave" style="top:0;height:70px" viewBox="0 0 100 20" preserveAspectRatio="none" aria-hidden="true">
      <path d="M0 0H100V6C70 14 35 2 0 12Z" fill="#ffffff"/>
      <path d="M0 12C35 2 70 14 100 6V9C70 17 35 5 0 15Z" fill="#3b4045"/>
    </svg>
    <div class="brand on-blue"><span class="brand-mark"></span>Kestrel Vale Realty</div>
    <div class="folder-address">
      <strong>Kestrel Vale Realty Ltd</strong><br>
      PO Box 4120<br>
      Tauranga 3140<br>
      T: 07 555 0142<br>
      E: hello@kvtp.co.nz
    </div>
  </div>
  <div class="folder-panel folder-front">
    <svg class="wave" style="top:0;height:60px" viewBox="0 0 100 20" preserveAspectRatio="none" aria-hidden="true">
      <path d="M0 0H100V10C70 3 40 14 0 5Z" fill="#3b4045"/>
      <path d="M0 0H100V6C70 0 40 10 0 2Z" fill="#2a9fd8"/>
    </svg>
    <div class="brand"><span class="brand-mark"></span>Kestrel Vale Realty</div>
    <p class="tagline">Save thousands in commission</p>
    <svg class="wave" style="bottom:0;height:80px" viewBox="0 0 100 26" preserveAspectRatio="none" aria-hidden="true">
      <path d="M0 10C30 2 65 14 100 4V26H0Z" fill="#3b4045"/>
      <path d="M0 14C30 6 65 18 100 8V26H0Z" fill="#2a9fd8"/>
    </svg>
    <span class="folder-url">www.kvtp.co.nz</span>
  </div>
  <div class="pocket pocket-left"><span class="pocket-mark"></span></div>
  <div class="pocket pocket-right"><span class="pocket-mark"></span></div>
</section>

<article class="sheet letterhead" aria-label="Letterhead">
  <div class="brand"><span class="brand-mark"></span>Kestrel Vale Realty</div>
  <span class="letter-tag">Save thousands in commission</span>
  <div class="letter-body">
    <p>Dear Client,</p>
    <p>Thank you for considering us to sell your home. Our team offers a fixed fee service that keeps more of the sale price in your pocket while giving your property strong exposure.</p>
    <p>We combine online listings, open homes and local knowledge to find the right buyer quickly. You stay informed at every step and decide how your home is presented.</p>
    <p>Please call us to arrange a free appraisal. We look forward to working with you.</p>
    <p>Kind regards,</p>
    <div class="signature-line"></div>
    <p>Dana Whitlow<br>Sales Manager</p>
  </div>
  <svg class="wave" style="bottom:0;height:42px" viewBox="0 0 100 14" preserveAspectRatio="none" aria-hidden="true">
    <path d="M0 4C30 0 65 8 100 2V14H0Z" fill="#3b4045"/>
    <path d="M0 7C30 3 65 11 100 5V14H0Z" fill="#2a9fd8"/>
  </svg>
  <span class="letter-footer">PO Box 4120, Tauranga 3140 · T: 07 555 0142</span>
</article>

<div class="sheet card card-front" aria-label="Business card front">
  <svg class="wave" style="top:0;height:20px" viewBox="0 0 100 14" preserveAspectRatio="none" aria-hidden="true">
    <path d="M0 0H100V8C65 2 30 12 0 6Z" fill="#2a9fd8"/>
  </svg>
  <div class="brand"><span class="brand-mark"></span>Kestrel Vale Realty</div>
  <svg class="wave" style="bottom:0;height:22px" viewBox="0 0 100 14" preserveAspectRatio="none" aria-hidden="true">
    <path d="M0 5C30 0 65 9 100 2V14H0Z" fill="#3b4045"/>
    <path d="M0 8C30 3 65 12 100 5V14H0Z" fill="#2a9fd8"/>
  </svg>
</div>

<div class="sheet card card-back" aria-label="Business card back">
  <div class="brand"><span class="brand-mark"></span>Kestrel Vale Realty</div>
  <div class="card-details">
    <strong>Dana Whitlow</strong><br>
    Sales Consultant<br>
    M: 021 555 0187<br>
    dana@kvtp.co.nz
  </div>
  <svg class="wave" style="bottom:0;height:16px" viewBox="0 0 100 14" preserveAspectRatio="none" aria-hidden="true">
    <path d="M0 6C30 0 65 10 100 3V14H0Z" fill="#2a9fd8"/>
  </svg>
</div>

<div class="sheet slip" aria-label="Compliments slip">
  <div class="brand"><span class="brand-mark"></span>Kestrel Vale Realty</div>
  <div class="slip-details"><strong>Dana Whitlow</strong><br>Sales Consultant<br>021 555 0187</div>
  <svg class="wave" style="bottom:0;height:16px" viewBox="0 0 100 14" preserveAspectRatio="none" aria-hidden="true">
    <path d="M0 5C30 0 65 9 100 2V14H0Z" fill="#3b4045"/>
    <path d="M0 8C30 3 65 12 100 5V14H0Z" fill="#2a9fd8"/>
  </svg>
</div>

<div class="sheet registry" aria-label="Registry card">
  <h1>Seller Requests Registration</h1>
  <h2>Open House Registry</h2>
  <svg class="wave" style="bottom:0;height:30px" viewBox="0 0 100 14" preserveAspectRatio="none" aria-hidden="true">
    <path d="M0 4C30 0 65 9 100 2V14H0Z" fill="#3b4045"/>
    <path d="M0 7C30 3 65 12 100 5V14H0Z" fill="#2a9fd8"/>
  </svg>
</div>

</body>
</html>
```